Clean, creative business Wordpress Site

Our company is building a website via Wordpress and needs a clean, no fuss, modern looking design that reflects our company brand (see attached logos).

In addition, the company is a woman owned business (no middle-aged white guy stock photos please) and primarily works with the oil & gas industry. We would prefer no images with direct references to energy (rigs, windmills, solar panels, etc.). Part of our consulting is providing thought leadership around energy politics and policy so creative ways to incorporate that visually will be appreciated as well.

Site map of pages below:

Home
- About
- Team
- Expertise
- Blog

We prefer a header image that includes the company logo and easy to identify and navigate menus.

Target Market(s)

Energy professionals, Executives

Industry/Entity Type

Consulting

Font styles to use
Serif

Colors
85acd3
0255a3
cedeed
ffffff

Requirements
Must have
• Clean and easy to navigate, clear menus, simple design that reflects company logo.

```html
<!DOCTYPE html>
<html lang="en">
<head>
<meta charset="utf-8">
<title>Keystone Meridian</title>
<link href="https://fonts.googleapis.com/css2?family=Roboto+Condensed:wght@400;700&family=Roboto:wght@400;500;700&display=swap" rel="stylesheet">
<style>
:root{
  --brand:#0255a3;
  --brand-deep:#1b5a98;
  --sky:#85acd3;
  --pale:#cedeed;
  --white:#ffffff;
  --ink:#222222;
  --text:#555555;
  --line:#dcdcdc;
}
*{box-sizing:border-box;margin:0;padding:0}
html,body{width:1200px;height:3261px;overflow:hidden}
body{position:relative;background:var(--white);font-family:'Roboto',Arial,sans-serif;color:var(--text)}
.abs{position:absolute}
.topbar{left:0;top:0;width:1200px;height:35px;background:var(--brand);color:var(--white);font-size:13px}
.topbar .contact{position:absolute;right:74px;top:9px;display:flex;gap:22px;align-items:center}
.topbar .contact span{display:flex;align-items:center;gap:7px}
.header{left:0;top:35px;width:1200px;height:95px;background:var(--white)}
.brand{position:absolute;left:78px;top:26px;display:flex;align-items:center;gap:12px}
.brand-mark{width:34px;height:34px;border:3px solid var(--brand)}
.brand-name{font-family:'Roboto Condensed',Arial,sans-serif;font-weight:700;font-size:26px;color:var(--brand);letter-spacing:1px}
.nav{position:absolute;right:74px;top:37px;display:flex;gap:6px}
.nav a{font-family:'Roboto Condensed',Arial,sans-serif;font-weight:700;font-size:15px;color:var(--ink);text-decoration:none;padding:7px 12px}
.nav a.active{background:var(--brand);color:var(--white)}
.hero{left:0;top:130px;width:1200px;height:577px;background:linear-gradient(100deg,#cfd3d6 0%,#e6e3df 35%,#b9b2ab 60%,#e2e4e6 100%)}
.hero h1{position:absolute;left:74px;top:222px;font-family:'Roboto Condensed',Arial,sans-serif;font-weight:700;color:#1b1b1b;line-height:1.1;text-transform:uppercase}
.hero h1 .l1{display:block;font-size:46px;letter-spacing:1px}
.hero h1 .l2{display:block;font-size:34px;letter-spacing:.5px}
.welcome{left:74px;top:670px;width:1052px;height:308px;background:var(--white);box-shadow:0 6px 18px rgba(0,0,0,.15);text-align:center}
.welcome .kicker{margin-top:44px;font-size:19px;color:var(--ink);font-family:'Roboto Condensed',Arial,sans-serif}
.welcome h2{font-family:'Roboto Condensed',Arial,sans-serif;font-weight:700;font-size:28px;color:var(--brand);letter-spacing:1px}
.divider{display:flex;align-items:center;justify-content:center;gap:6px;margin:6px 0 20px}
.divider i{display:block;width:60px;height:1px;background:var(--sky)}
.divider b{display:block;width:9px;height:9px;border:2px solid var(--brand);border-radius:50%}
.welcome p{padding:0 28px;font-size:14px;line-height:25px;color:var(--text)}
.btn{display:inline-block;background:var(--sky);color:var(--white);font-size:13px;text-transform:uppercase;padding:12px 22px;box-shadow:0 2px 4px rgba(0,0,0,.2)}
.welcome .btn{position:absolute;left:459px;top:243px;width:134px;text-align:center}
.team{left:0;top:1002px;width:600px;height:502px;background:var(--brand-deep);color:var(--white)}
.team h2{position:absolute;left:74px;top:40px;font-family:'Roboto Condensed',Arial,sans-serif;font-weight:700;font-size:29px}
.team p{position:absolute;left:74px;top:100px;width:480px;font-size:14px;line-height:24px}
.team .btn{position:absolute;left:74px;top:412px}
.team-photo{left:600px;top:1002px;width:600px;height:502px;background:linear-gradient(180deg,#e9ebed 0%,#c3c7cc 45%,#3c4658 100%)}
.expertise{left:74px;top:1570px;width:1052px;height:289px;border:2px solid #e4e4e4}
.section-label{left:452px;top:1550px;width:296px;height:44px;background:var(--white);border:2px solid #e4e4e4;text-align:center;font-family:'Roboto Condensed',Arial,sans-serif;font-weight:700;font-size:28px;color:var(--ink);line-height:40px}
.skill{top:1632px;width:200px;text-align:center}
.skill .icon{width:88px;height:88px;margin:0 auto;border-radius:50%;background:var(--brand);display:flex;align-items:center;justify-content:center}
.skill h3{margin-top:18px;font-family:'Roboto',Arial,sans-serif;font-weight:500;font-size:21px;line-height:25px;color:#333}
.skill .plus{width:18px;height:18px;margin:12px auto 0;border:1.5px solid var(--sky);border-radius:50%;color:var(--sky);font-size:14px;line-height:15px}
.video{left:0;top:1904px;width:1200px;height:505px;background:var(--sky)}
.video-tab{left:409px;top:1950px;width:378px;height:52px;background:var(--brand);clip-path:polygon(14px 0,364px 0,378px 100%,0 100%);color:var(--white);text-align:center;font-family:'Roboto Condensed',Arial,sans-serif;font-weight:700;font-size:29px;line-height:54px}
.video-frame{left:298px;top:2002px;width:604px;height:361px;background:var(--white);padding:14px;box-shadow:0 4px 10px rgba(0,0,0,.2)}
.video-still{width:100%;height:100%;background:linear-gradient(120deg,#3e5b78 0%,#8aa6bf 45%,#9cb2c6 60%,#2f4e6d 100%);display:flex;align-items:center;justify-content:center}
.play{width:82px;height:82px;border:4px solid var(--white);border-radius:50%;display:flex;align-items:center;justify-content:center}
.blogs-title{left:0;top:2448px;width:1200px;text-align:center;font-family:'Roboto Condensed',Arial,sans-serif;font-weight:700;font-size:29px;color:var(--ink)}
.post{top:2522px;width:242px;height:409px;border:2px solid var(--brand);background:var(--white)}
.post .thumb{height:180px}
.post h4{margin:16px 14px 0;font-size:15px;line-height:22px;font-weight:700;color:var(--ink)}
.post .date{margin:6px 14px 0;font-size:12px;color:#444}
.post p{margin:10px 14px 0;font-size:13px;line-height:22px;color:#555}
.post .more{margin:8px 14px 0;font-size:13px;color:var(--sky)}
.footer{left:0;top:2978px;width:1200px;height:283px;background:var(--brand);color:var(--white)}
.footer .brand{left:82px;top:44px}
.footer .brand-mark{border-color:var(--white)}
.footer .brand-name{color:var(--white)}
.f-item{position:absolute;display:flex;gap:16px}
.f-item small{display:block;font-size:11px;text-transform:uppercase;opacity:.85}
.f-item div{font-size:19px;line-height:23px}
.msg{display:inline-block;margin-top:12px;background:#0c2f6b;border-radius:16px;padding:7px 18px;font-size:12px;font-weight:700;text-transform:uppercase}
.social{position:absolute;left:812px;top:160px;display:flex;gap:6px}
.social i{display:block;width:30px;height:30px;border:2px solid var(--white);border-radius:50%}
.copyright{position:absolute;left:0;top:244px;width:1200px;text-align:center;font-size:13px}
</style>
</head>
<body>
<div class="abs topbar">
  <div class="contact">
    <span><svg width="14" height="14" viewBox="0 0 24 24"><path d="M6.6 10.8a15 15 0 0 0 6.6 6.6l2.2-2.2c.3-.3.7-.4 1-.2 1.1.4 2.3.6 3.6.6.6 0 1 .4 1 1V20c0 .6-.4 1-1 1A17 17 0 0 1 3 4c0-.6.4-1 1-1h3.5c.6 0 1 .4 1 1 0 1.3.2 2.5.6 3.6.1.3 0 .7-.2 1z" fill="#fff"/></svg>123-456-5555</span>
    <span><svg width="16" height="12" viewBox="0 0 16 12"><rect width="16" height="12" fill="#fff"/><path d="M0 0l8 7 8-7" stroke="#0255a3" stroke-width="1.5" fill="none"/></svg>info@keystonemeridian.com</span>
  </div>
</div>

<header class="abs header">
  <div class="brand"><span class="brand-mark"></span><span class="brand-name">KEYSTONE MERIDIAN</span></div>
  <nav class="nav">
    <a class="active" href="#">HOME</a><a href="#">ABOUT</a><a href="#">TEAM</a><a href="#">EXPERTISE</a><a href="#">BLOG</a>
  </nav>
</header>

<section class="abs hero" role="img" aria-label="Photo of two colleagues smiling in an office meeting, one holding a tablet">
  <h1><span class="l1">Lorem ipsum dolor sit</span><span class="l2">Ametc onsectetur adipiscing elit</span></h1>
</section>

<section class="abs welcome">
  <div class="kicker">WELCOME TO</div>
  <h2>KEYSTONE MERIDIAN</h2>
  <div class="divider"><i></i><b></b><i></i></div>
  <p>Lorem ipsum dolor sit amet, consectetur adipiscing elit, sed do eiusmod tempor incididunt ut labore et dolore magna aliqua. Ut enim ad minim veniam, quis nostrud exercitation ullamco laboris nisi ut aliquip ex ea commodo consequat. Duis aute irure dolor in reprehenderit in voluptate velit esse cillum dolore eu fugiat nulla pariatur. Excepteur sint occaecat cupidatat non proident, sunt in culpa qui officia deserunt mollit anim id est laborum.</p>
  <span class="btn">Learn more</span>
</section>

<section class="abs team">
  <h2>OUR TEAM</h2>
  <p>Lorem ipsum dolor sit amet, consectetur adipiscing elit, sed do eiusmod tempor incididunt ut labore et dolore magna aliqua. Ut enim ad minim veniam, quis nostrud exercitation ullamco laboris nisi ut aliquip ex ea commodo consequat. Duis aute irure dolor in reprehenderit in voluptate velit esse cillum dolore eu fugiat nulla pariatur. Excepteur sint occaecat cupidatat non proident, sunt in culpa qui officia deserunt mollit anim id est laborum. Lorem ipsum dolor sit amet, consectetur adipiscing elit, sed do eiusmod tempor incididunt ut labore et dolore magna aliqua. Ut enim ad minim veniam, quis nostrud exercitation ullamco laboris nisi ut aliquip ex ea commodo consequat. Duis aute irure dolor in reprehenderit in voluptate velit esse cillum dolore eu fugiat nulla pariatur.</p>
  <span class="btn">Learn more</span>
</section>
<div class="abs team-photo" role="img" aria-label="Photo of a diverse business team standing together in a bright office"></div>

<section class="abs expertise"></section>
<div class="abs section-label">OUR EXPERTISE</div>

<div class="abs skill" style="left:85px">
  <div class="icon"><svg width="44" height="36" viewBox="0 0 44 36" fill="#fff"><circle cx="22" cy="9" r="6"/><circle cx="10" cy="12" r="5"/><circle cx="34" cy="12" r="5"/><path d="M12 34c0-8 4-14 10-14s10 6 10 14z"/><path d="M1 32c0-7 3-12 9-12 2 0 3 .5 4 1-2 3-3 7-3 11z"/><path d="M43 32c0-7-3-12-9-12-2 0-3 .5-4 1 2 3 3 7 3 11z"/></svg></div>
  <h3>Community<br>Engagement</h3><div class="plus">+</div>
</div>
<div class="abs skill" style="left:292px">
  <div class="icon"><svg width="34" height="40" viewBox="0 0 34 40"><path d="M3 2h20l8 8v28H3z" fill="none" stroke="#fff" stroke-width="2.5"/><path d="M9 16h16M9 22h16M9 28h11" stroke="#fff" stroke-width="2.5"/></svg></div>
  <h3>Navigating<br>Policy</h3><div class="plus">+</div>
</div>
<div class="abs skill" style="left:500px">
  <div class="icon"><svg width="40" height="36" viewBox="0 0 40 36" fill="#fff"><rect x="2" y="2" width="36" height="32" fill="none" stroke="#fff" stroke-width="2.5"/><rect x="8" y="20" width="5" height="10"/><rect x="15" y="14" width="5" height="16"/><rect x="22" y="17" width="5" height="13"/><rect x="29" y="9" width="5" height="21"/></svg></div>
  <h3>Investor<br>Relations</h3><div class="plus">+</div>
</div>
<div class="abs skill" style="left:707px">
  <div class="icon"><svg width="32" height="42" viewBox="0 0 32 42"><path d="M16 3a12 12 0 0 0-7 22v6h14v-6A12 12 0 0 0 16 3z" fill="none" stroke="#fff" stroke-width="2.5"/><path d="M10 35h12M12 39h8" stroke="#fff" stroke-width="2.5"/></svg></div>
  <h3>Energy<br>Access</h3><div class="plus">+</div>
</div>
<div class="abs skill" style="left:915px">
  <div class="icon"><svg width="38" height="38" viewBox="0 0 38 38" stroke="#fff" stroke-width="3" fill="none"><path d="M3 3l11 11M14 6v8H6M35 3L24 14M24 6v8h8M3 35l11-11M14 32v-8H6M35 35L24 24M24 32v-8h8"/></svg></div>
  <h3>Deescalating<br>Conflict</h3><div class="plus">+</div>
</div>

<section class="abs video"></section>
<div class="abs video-tab">WATCH OUR VIDEO</div>
<div class="abs video-frame">
  <div class="video-still" role="img" aria-label="Video still of a business handshake">
    <div class="play"><svg width="28" height="32" viewBox="0 0 28 32"><path d="M4 2l22 14L4 30z" fill="#fff"/></svg></div>
  </div>
</div>

<h2 class="abs blogs-title">LATEST BLOGS</h2>
<article class="abs post" style="left:74px">
  <div class="thumb" role="img" aria-label="Photo of a professional working at a laptop" style="background:linear-gradient(135deg,#4d5f78,#b7c3cf)"></div>
  <h4>Lorem ipsum dolor sit amet, consectetur adipiscing elit</h4><div class="date">NOV 17, 2016</div>
  <p>Sed do eiusmod tempor incididunt ut labore et dolore magna aliqua. Ut enim ad minim veniam, quis nostrud.</p><div class="more">Read More»</div>
</article>
<article class="abs post" style="left:346px">
  <div class="thumb" role="img" aria-label="Photo of colleagues in conversation" style="background:linear-gradient(135deg,#d9dadc,#6c6f76)"></div>
  <h4>Lorem ipsum dolor sit amet, consectetur adipiscing elit</h4><div class="date">NOV 17, 2016</div>
  <p>Sed do eiusmod tempor incididunt ut labore et dolore magna aliqua. Ut enim ad minim veniam, quis nostrud.</p><div class="more">Read More»</div>
</article>
<article class="abs post" style="left:615px">
  <div class="thumb" role="img" aria-label="Photo of a team meeting around a table" style="background:linear-gradient(135deg,#cfc9c2,#7e858e)"></div>
  <h4>Lorem ipsum dolor sit amet, consectetur adipiscing elit</h4><div class="date">NOV 17, 2016</div>
  <p>Sed do eiusmod tempor incididunt ut labore et dolore magna aliqua. Ut enim ad minim veniam, quis nostrud.</p><div class="more">Read More»</div>
</article>
<article class="abs post" style="left:885px">
  <div class="thumb" role="img" aria-label="Photo of a group gathered in a modern workspace" style="background:linear-gradient(135deg,#3a3f47,#a8927a)"></div>
  <h4>Lorem ipsum dolor sit amet, consectetur adipiscing elit</h4><div class="date">NOV 17, 2016</div>
  <p>Sed do eiusmod tempor incididunt ut labore et dolore magna aliqua. Ut enim ad minim veniam, quis nostrud.</p><div class="more">Read More»</div>
</article>

<footer class="abs footer">
  <div class="brand"><span class="brand-mark"></span><span class="brand-name">KEYSTONE MERIDIAN</span></div>
  <div class="f-item" style="left:420px;top:38px">
    <svg width="30" height="30" viewBox="0 0 24 24"><path d="M6.6 10.8a15 15 0 0 0 6.6 6.6l2.2-2.2c.3-.3.7-.4 1-.2 1.1.4 2.3.6 3.6.6.6 0 1 .4 1 1V20c0 .6-.4 1-1 1A17 17 0 0 1 3 4c0-.6.4-1 1-1h3.5c.6 0 1 .4 1 1 0 1.3.2 2.5.6 3.6.1.3 0 .7-.2 1z" fill="none" stroke="#fff" stroke-width="1.5"/></svg>
    <div><small>Call</small>123-456-5555</div>
  </div>
  <div class="f-item" style="left:424px;top:112px">
    <svg width="26" height="34" viewBox="0 0 26 34"><path d="M13 2a11 11 0 0 0-11 11c0 8 11 19 11 19s11-11 11-19A11 11 0 0 0 13 2z" fill="none" stroke="#fff" stroke-width="2"/><circle cx="13" cy="13" r="4" fill="none" stroke="#fff" stroke-width="2"/></svg>
    <div><small>Visit</small>Your Company LTD.<br>Street Name, 000000<br>City Name</div>
  </div>
  <div class="f-item" style="left:760px;top:38px">
    <svg width="30" height="30" viewBox="0 0 30 30"><path d="M4 26l3-9L21 3l6 6-14 14z M7 17l6 6" fill="none" stroke="#fff" stroke-width="2"/></svg>
    <div><small>Write</small>info@keystonemeridian.com<br><span class="msg">Message us</span></div>
  </div>
  <div class="social"><i></i><i></i></div>
  <div class="copyright">© 2017 Keystone Meridian. All rights reserved.</div>
</footer>
</body>
</html>
```